Amber Ridge Ventures, LLC Business Card

We need a logo that will be embossed or printed in a singular light color for Business Cards. Would be interested in seeing a Cypress Tree graphic. Our company name is Amber Ridge Ventures, LLC. Business Card layout and graphic should project imagine of confidence, integrity and strength.

```html
<!DOCTYPE html>
<html lang="en">
<head>
<meta charset="utf-8">
<title>Amber Ridge Ventures, LLC — Business Card</title>
<link rel="stylesheet" href="https://fonts.googleapis.com/css2?family=Cinzel:wght@400;600&family=Questrial&display=swap">
<style>
  :root {
    --backdrop: #e8e5e0;
    --card: #f7f7f7;
    --ink: #1c1c1c;
    --panel: #2b2d30;
    --panel-text: #d9dadc;
    --accent: #3fa9e0;
    --muted: #6d6f72;
  }
  * { margin: 0; padding: 0; box-sizing: border-box; }
  html, body { width: 1200px; height: 1000px; overflow: hidden; }
  body { background: var(--backdrop); position: relative; font-family: "Questrial", sans-serif; }

  .card {
    position: absolute;
    width: 560px;
    height: 320px;
    background: var(--card);
    box-shadow: 0 10px 28px rgba(0,0,0,0.18);
    overflow: hidden;
  }

  /* Front */
  .card-front { left: 90px; top: 520px; }
  .front-mark {
    position: absolute; left: 50%; top: 46px;
    width: 104px; height: 104px; margin-left: -52px;
    border-radius: 50%; background: var(--ink);
  }
  .front-name {
    position: absolute; left: 0; right: 0; top: 176px;
    text-align: center;
    font-family: "Cinzel", serif; font-weight: 600;
    font-size: 30px; letter-spacing: 0.5px; color: var(--ink);
  }
  .front-rule {
    position: absolute; left: 70px; right: 70px; top: 222px;
    height: 2px; background: var(--ink);
  }
  .front-suffix {
    position: absolute; left: 0; right: 0; top: 236px;
    text-align: center;
    font-family: "Cinzel", serif; font-weight: 600;
    font-size: 20px; color: var(--ink);
  }

  /* Back */
  .card-back { left: 550px; top: 110px; }
  .back-brand { position: absolute; left: 40px; top: 34px; display: flex; align-items: center; gap: 10px; }
  .back-mark { width: 74px; height: 74px; border-radius: 50%; background: var(--ink); }
  .back-brand-name {
    font-family: "Cinzel", serif; font-weight: 600; font-size: 13px;
    color: var(--ink); width: 110px; line-height: 1.25;
  }
  .person { position: absolute; left: 300px; top: 96px; right: 0; }
  .person-name { font-size: 26px; font-weight: 400; color: var(--ink); letter-spacing: 0.5px; -webkit-text-stroke: 0.4px var(--ink); }
  .person-role { font-size: 12px; color: var(--muted); margin-top: 2px; }
  .person-rule { height: 2px; background: var(--accent); margin-top: 6px; }

  .contact-panel {
    position: absolute; left: 270px; right: 0; top: 160px; height: 110px;
    background: var(--panel);
    padding: 20px 0 0 20px;
    display: flex; gap: 14px;
  }
  .contact-icons { display: flex; flex-direction: column; gap: 8px; padding-top: 2px; }
  .contact-icons svg { display: block; }
  .contact-lines { list-style: none; color: var(--panel-text); font-size: 15px; line-height: 1.45; letter-spacing: 0.5px; }

  .base-band {
    position: absolute; left: 0; right: 0; bottom: 0; height: 24px;
    background: linear-gradient(90deg, #1e1f21, #3a3c3f);
  }
</style>
</head>
<body>

  <section class="card card-front" aria-label="Business card front">
    <div class="front-mark"></div>
    <div class="front-name">Amber Ridge Ventures</div>
    <div class="front-rule"></div>
    <div class="front-suffix">LLC</div>
  </section>

  <section class="card card-back" aria-label="Business card back">
    <div class="back-brand">
      <div class="back-mark"></div>
      <div class="back-brand-name">Amber Ridge Ventures, LLC</div>
    </div>

    <div class="person">
      <div class="person-name">Employee Name</div>
      <div class="person-role">Designation</div>
      <div class="person-rule"></div>
    </div>

    <div class="contact-panel">
      <div class="contact-icons">
        <svg width="16" height="16" viewBox="0 0 16 16" aria-label="Address">
          <rect x="0.5" y="0.5" width="15" height="15" rx="2" fill="none" stroke="#3fa9e0"/>
          <path d="M8 3.5a3 3 0 0 1 3 3c0 2.2-3 5.5-3 5.5s-3-3.3-3-5.5a3 3 0 0 1 3-3z" fill="#3fa9e0"/>
        </svg>
        <svg width="16" height="16" viewBox="0 0 16 16" aria-label="Phone">
          <rect x="0.5" y="0.5" width="15" height="15" rx="2" fill="none" stroke="#3fa9e0"/>
          <rect x="5" y="3" width="6" height="10" rx="1" fill="#3fa9e0"/>
        </svg>
        <svg width="16" height="16" viewBox="0 0 16 16" aria-label="Phone">
          <rect x="0.5" y="0.5" width="15" height="15" rx="2" fill="none" stroke="#3fa9e0"/>
          <rect x="5" y="3" width="6" height="10" rx="1" fill="#3fa9e0"/>
        </svg>
      </div>
      <ul class="contact-lines">
        <li>Address</li>
        <li>(123) 456 7890</li>
        <li>(123) 456 789</li>
      </ul>
    </div>

    <div class="base-band"></div>
  </section>

</body>
</html>
```